Insurance company needs a business card design

We need a business card design for a Massachusetts-based insurance company Veloria Insurance, LLC. We provide auto insurance to Hispanic (Spanish- or Portuguese-speaking) immigrants in the United States. We will give these business cards to auto dealers where such customers typically go to purchase vehicles. We will provide a solution to the dealers to provide easy insurance to the customers buying cars at their dealerships. Veloria is the Spanish word for protection.
Contact Information for Business Card
Name, Designation, Company Name, Address, Phone Number, Email, Website
Look and feel
Each slider illustrates characteristics of the customer's brand and the style your logo design should communicate.

```html
<!DOCTYPE html>
<html lang="en">
<head>
<meta charset="UTF-8">
<title>Veloria Insurance — Business Card</title>
<link href="https://fonts.googleapis.com/css2?family=Montserrat:wght@700;800&family=Roboto:wght@400;500&display=swap" rel="stylesheet">
<style>
  :root {
    --stage: #2e2e2e;
    --card-blue: #12598a;
    --card-blue-light: #1a6a9c;
    --card-blue-deep: #0f4f7d;
    --accent-orange: #f08a24;
    --text-white: #ffffff;
  }
  * { box-sizing: border-box; margin: 0; padding: 0; }
  html, body {
    width: 1200px; height: 900px; overflow: hidden;
    background: var(--stage);
  }
  .stage {
    width: 1200px; height: 900px;
    display: flex; align-items: center; justify-content: center; gap: 40px;
  }
  .card {
    position: relative;
    width: 540px; height: 309px;
    background: radial-gradient(circle at 35% 20%, var(--card-blue-light), var(--card-blue) 55%, var(--card-blue-deep));
    overflow: hidden;
    color: var(--text-white);
    font-family: "Roboto", Arial, sans-serif;
  }
  .wordmark {
    display: flex; align-items: center; gap: 10px;
    font-family: "Montserrat", Arial, sans-serif;
    font-weight: 800;
    color: var(--text-white);
    text-transform: uppercase;
    letter-spacing: 1px;
  }
  .wordmark-square {
    background: var(--accent-orange);
    flex: none;
  }
  /* info side */
  .card-info .wordmark {
    position: absolute; left: 36px; top: 34px;
    font-size: 22px;
  }
  .card-info .wordmark-square { width: 16px; height: 16px; }
  .contact {
    position: absolute; left: 36px; top: 96px;
  }
  .contact-name {
    font-family: "Montserrat", Arial, sans-serif;
    font-weight: 800; font-size: 17px;
    color: var(--accent-orange);
    text-transform: uppercase;
  }
  .contact-title { font-size: 12px; margin-top: 2px; }
  .contact-address { font-size: 12px; line-height: 16px; margin-top: 14px; }
  .contact-lines { list-style: none; margin-top: 12px; font-size: 12px; line-height: 17px; }
  .contact-lines li { display: flex; align-items: center; gap: 7px; }
  .contact-lines svg { width: 10px; height: 10px; flex: none; }
  .brand-disc {
    position: absolute; right: -40px; bottom: -40px;
    width: 260px; height: 260px; border-radius: 50%;
    background: rgba(255,255,255,0.08);
  }
  /* logo side */
  .card-logo { display: flex; align-items: center; justify-content: center; }
  .card-logo .wordmark { font-size: 30px; gap: 14px; }
  .card-logo .wordmark-square { width: 22px; height: 22px; }
</style>
</head>
<body>
<main class="stage">
  <section class="card card-info">
    <div class="wordmark"><span class="wordmark-square"></span>Veloria Insurance</div>
    <div class="contact">
      <p class="contact-name">Daniel Reyes</p>
      <p class="contact-title">Founder &amp; CEO</p>
      <p class="contact-address">48 Harbor Street Suite 310<br>Boston, MA, USA</p>
      <ul class="contact-lines">
        <li><svg viewBox="0 0 10 10"><path d="M2 1l2 2-1 1.2c.6 1.2 1.6 2.2 2.8 2.8L7 6l2 2-1.3 1.3C4.5 9 1 5.5.7 2.3z" fill="var(--accent-orange)"/></svg>(866) 555-0142</li>
        <li><svg viewBox="0 0 10 10"><rect x="0.5" y="2" width="9" height="6.5" fill="var(--accent-orange)"/><path d="M.5 2l4.5 3.5L9.5 2" stroke="var(--card-blue)" stroke-width="1" fill="none"/></svg>info@veloriainsurance.com</li>
        <li><svg viewBox="0 0 10 10"><circle cx="5" cy="5" r="4.2" stroke="var(--accent-orange)" stroke-width="1" fill="none"/><ellipse cx="5" cy="5" rx="1.8" ry="4.2" stroke="var(--accent-orange)" stroke-width="0.8" fill="none"/><path d="M.8 5h8.4" stroke="var(--accent-orange)" stroke-width="0.8"/></svg>www.veloriainsurance.com</li>
      </ul>
    </div>
    <div class="brand-disc" aria-hidden="true"></div>
  </section>

  <section class="card card-logo">
    <div class="wordmark"><span class="wordmark-square"></span>Veloria Insurance</div>
  </section>
</main>
</body>
</html>
```